Business card design needed

I need to display a copy of one of my paintings on front,
with my contact details displayed effectively within the painting.
On the back, my Logo needs to be displayed.
Font used should be artistic, but legible.
A high quality GLOSS Paper

Target Market(s)

Business people who purchase my Art for their premises and Boardrooms but also home owners both Traditional and Modern enthusiasts.

Industry/Entity Type

Business

Contact Information for Business Card

Artist /Interior Designer- Marla Fenwick
Specializing in Oils on Canvas
Co-ordinate Colours in Home or Office
Over 25 years experience
mobile: 0452 908146
email: marla.f@quorvel.net.au
P.O. Box 518
Double Bay 1360 NSW

Requirements
Must have
• Good visual of painting, well proportioned.
Your can play with the description of Artist as long as it appeals to the above clientele.
Choose a painting which allows the potential client to see the text but showcases

the canvas too.

```html
<!DOCTYPE html>
<html lang="en">
<head>
<meta charset="utf-8">
<title>Marla Fenwick — Business Card</title>
<link rel="stylesheet" href="https://fonts.googleapis.com/css2?family=Marcellus&family=Marcellus+SC&family=Parisienne&display=swap">
<style>
  :root {
    --page: #ffffff;
    --card-dark: #16140f;
    --band: rgba(22, 20, 16, 0.78);
    --paint-violet: #5a55b8;
    --paint-lilac: #8d86d6;
    --paint-deep: #1d1a1c;
    --paint-amber: #7a5a22;
    --text-light: #f1efe8;
    --accent-yellow: #f2d51a;
    --gold: #e6c020;
    --olive-glow: #4d4220;
    --olive-edge: #15130e;
  }
  * { margin: 0; padding: 0; box-sizing: border-box; }
  html, body {
    width: 1200px; height: 1000px; overflow: hidden;
    background: var(--page);
  }
  .sheet { position: relative; width: 1200px; height: 1000px; }

  .card {
    position: absolute; left: 187px; width: 797px; height: 461px;
    overflow: hidden; background: var(--card-dark);
  }
  .card--front { top: 25px; }
  .card--back { top: 509px; }

  /* front */
  .painting {
    position: absolute; inset: 0;
    background:
      radial-gradient(ellipse 22% 40% at 36% 45%, var(--paint-lilac) 0%, rgba(90,85,184,0.55) 45%, transparent 75%),
      radial-gradient(ellipse 18% 38% at 76% 48%, var(--paint-lilac) 0%, rgba(90,85,184,0.55) 45%, transparent 75%),
      radial-gradient(ellipse 14% 30% at 55% 35%, rgba(122,90,34,0.45) 0%, transparent 70%),
      radial-gradient(ellipse 60% 60% at 50% 30%, #2b2630 0%, var(--paint-deep) 70%);
  }
  .info-band {
    position: absolute; left: 0; right: 0; top: 293px; bottom: 0;
    background: var(--band);
  }
  .details {
    position: absolute; left: 53px; top: 282px;
    color: var(--text-light);
    font-family: "Marcellus SC", "Marcellus", serif;
  }
  .details__name {
    font-family: "Parisienne", cursive;
    font-size: 44px; line-height: 52px; color: var(--text-light);
    margin-left: -2px;
  }
  .details__role {
    font-family: "Marcellus", serif;
    font-weight: 700; font-size: 15px; letter-spacing: 0.8px;
    text-transform: uppercase; line-height: 22px; margin-top: -6px;
    text-shadow: 0.4px 0 0 currentColor;
  }
  .details__line {
    font-size: 16px; letter-spacing: 0.9px; line-height: 22px;
    text-transform: uppercase;
  }
  .contact {
    position: absolute; left: 470px; top: 327px;
    list-style: none; color: var(--text-light);
    font-family: "Marcellus", serif; font-size: 16px; letter-spacing: 0.9px;
    text-transform: uppercase;
  }
  .contact__item { display: flex; align-items: center; height: 22px; }
  .contact__item--phone { font-weight: 700; text-shadow: 0.4px 0 0 currentColor; }
  .contact__icon { width: 18px; height: 18px; margin-right: 8px; flex: none; }
  .contact__spacer { width: 18px; margin-right: 8px; flex: none; }

  /* back */
  .card--back {
    background: radial-gradient(ellipse 75% 85% at 52% 18%, var(--olive-glow) 0%, #2a2414 50%, var(--olive-edge) 100%);
  }
  .brand { position: absolute; left: 108px; top: 188px; }
  .brand__name {
    font-family: "Marcellus", serif;
    font-size: 46px; letter-spacing: 1.5px; line-height: 56px;
    text-transform: uppercase; color: var(--gold);
  }
  .brand__tagline {
    font-family: "Marcellus SC", "Marcellus", serif;
    font-size: 23px; letter-spacing: 2.6px; color: var(--text-light);
    margin-top: -2px; white-space: nowrap;
  }
</style>
</head>
<body>
<main class="sheet">
  <section class="card card--front">
    <div class="painting" role="img" aria-label="Oil painting of hanging purple wisteria blossoms with amber and green stems on a dark background"></div>
    <div class="info-band"></div>
    <div class="details">
      <p class="details__name">Marla Fenwick</p>
      <p class="details__role">Artist / Interior Designer</p>
      <p class="details__line">Specializing in oils on canvas</p>
      <p class="details__line">Co-ordinate colours in home or office</p>
      <p class="details__line">Over 25 years experience</p>
    </div>
    <ul class="contact">
      <li class="contact__item contact__item--phone">
        <svg class="contact__icon" viewBox="0 0 24 24" aria-hidden="true"><path fill="#f2d51a" d="M6.6 2.5c.6-.3 1.3-.1 1.6.5l1.9 3.6c.3.6.1 1.3-.4 1.7L8 9.4c.9 2.6 3.7 5.5 6.4 6.5l1.2-1.7c.4-.5 1.1-.7 1.7-.4l3.6 1.9c.6.3.8 1 .5 1.6l-1.3 2.6c-.4.8-1.300 1.3-2.2 1.1C10.6 19.6 4.4 13.4 3 6.1c-.2-.9.3-1.8 1.1-2.2z"/></svg>
        0452 908146
      </li>
      <li class="contact__item">
        <svg class="contact__icon" viewBox="0 0 24 24" aria-hidden="true"><rect x="2" y="5" width="20" height="14" fill="#f2d51a"/><path d="M2.5 5.5 12 13l9.5-7.5" fill="none" stroke="#16140f" stroke-width="1.6"/></svg>
        marla.f@quorvel.net.au
      </li>
      <li class="contact__item">
        <svg class="contact__icon" viewBox="0 0 24 24" aria-hidden="true"><path fill="#f2d51a" d="M12 1.5c-3.9 0-7 3-7 6.9 0 5 7 14.1 7 14.1s7-9.1 7-14.1c0-3.9-3.1-6.9-7-6.900z"/><circle cx="12" cy="8.4" r="2.6" fill="#16140f"/></svg>
        P.O. Box 518
      </li>
      <li class="contact__item">
        <span class="contact__spacer"></span>
        Kestrel Bay, 2094 NSW
      </li>
    </ul>
  </section>

  <section class="card card--back">
    <div class="brand">
      <p class="brand__name">Marla Fenwick Art</p>
      <p class="brand__tagline">Original Paintings for Home &amp; Office</p>
    </div>
  </section>
</main>
</body>
</html>
```